Fontenot Bayou Grillhouse (Owners Card)

Need a classy, but modern business card. I have included a promotional card for the steakhouse. I need one for myself (the owner) that is more professional.

Target Market(s)

General Public

Industry/Entity Type

Food service

Contact Information for Business Card

Name, business address, phone number, email, logo

Font styles to use
Serif
Sans Serif
Decorative
Script

Requirements
Must have
• My name (Darvel Pruitt), business address (327 Oakmere Street), phone number (510) 493-2615, email (Dpruittkr4@mailvane.example. On the back of the card: Psalms 27 1 The LORD is my light and my salvation— whom shall I fear? The LORD is the stronghold of my life— of whom shall I be afraid? 2 When the wicked advance against me to devour me, it is my enemies and my foes who will stumble and fall. 3 Though an army besiege me, my heart will not fear; though war break out against me, even then I will be confident.
Nice to have
• Something that’s bold, but modern and professional.

```html
<!DOCTYPE html>
<html lang="en">
<head>
<meta charset="utf-8">
<title>Fontenot Bayou Grillhouse – Owner Card</title>
<link href="https://fonts.googleapis.com/css2?family=Cinzel:wght@600&family=Open+Sans:wght@400;700&display=swap" rel="stylesheet">
<style>
  :root {
    --stage: #3a3a3a;
    --card: #050505;
    --ink: #ffffff;
    --green: #8cc63f;
    --yellow: #f4d21f;
    --orange: #f08a2c;
    --red: #e8321e;
    --pink: #d4145a;
    --brand: #f2a23a;
  }
  * { margin: 0; padding: 0; box-sizing: border-box; }
  html, body { width: 1200px; height: 689px; overflow: hidden; }
  body {
    background: var(--stage);
    font-family: "Open Sans", Arial, sans-serif;
    color: var(--ink);
    position: relative;
  }
  .card {
    position: absolute;
    top: 190px;
    width: 540px;
    height: 310px;
    background: var(--card);
    border-radius: 22px;
    overflow: hidden;
  }
  .card--back { left: 40px; }
  .card--front { left: 620px; }

  /* Wordmark stand-in */
  .wordmark {
    display: flex;
    align-items: center;
    gap: 10px;
    font-family: "Open Sans", Arial, sans-serif;
    font-weight: 700;
    color: var(--brand);
    line-height: 1.15;
  }
  .wordmark__dot {
    width: 14px; height: 14px;
    border-radius: 50%;
    background: var(--brand);
    flex: none;
  }

  /* Back */
  .card--back .wordmark {
    justify-content: center;
    margin-top: 34px;
    font-size: 20px;
  }
  .verse-title {
    text-align: center;
    font-weight: 700;
    font-size: 15px;
    margin-top: 16px;
  }
  .verses {
    list-style: none;
    margin: 10px 40px 0 30px;
  }
  .verse {
    display: flex;
    gap: 22px;
    font-size: 12.5px;
    line-height: 1.55;
    margin-bottom: 4px;
  }
  .verse__num { width: 10px; flex: none; }

  /* Front */
  .band {
    position: absolute;
    inset: 0;
  }
  .card--front .wordmark {
    position: absolute;
    left: 36px;
    top: 118px;
    width: 200px;
    font-size: 19px;
  }
  .divider {
    position: absolute;
    left: 258px;
    top: 46px;
    width: 2px;
    height: 130px;
    background: linear-gradient(var(--red), var(--orange));
  }
  .owner {
    position: absolute;
    left: 278px;
    top: 46px;
  }
  .owner__name {
    font-family: "Cinzel", Georgia, serif;
    font-weight: 600;
    font-size: 27px;
    letter-spacing: 1px;
    background: linear-gradient(90deg, var(--yellow), var(--orange) 45%, var(--red));
    -webkit-background-clip: text;
    background-clip: text;
    color: transparent;
    margin-bottom: 8px;
  }
  .contact { list-style: none; }
  .contact__item {
    display: flex;
    align-items: center;
    gap: 10px;
    font-size: 14px;
    line-height: 1.75;
  }
  .contact__icon { width: 14px; height: 14px; flex: none; }
</style>
</head>
<body>

<section class="card card--back">
  <div class="wordmark"><span class="wordmark__dot"></span>Fontenot Bayou Grillhouse</div>
  <h2 class="verse-title">Psalms 27</h2>
  <ol class="verses">
    <li class="verse"><span class="verse__num">1</span><span>The LORD is my light and my salvation— whom shall I fear? The LORD is the stronghold of my life— of whom shall I be afraid?</span></li>
    <li class="verse"><span class="verse__num">2</span><span>When the wicked advance against me to devour me, it is my enemies and my foes who will stumble and fall.</span></li>
    <li class="verse"><span class="verse__num">3</span><span>Though an army besiege me, my heart will not fear; though war break out against me, even then I will be confident.</span></li>
  </ol>
</section>

<section class="card card--front">
  <svg class="band" width="540" height="310" viewBox="0 0 540 310" aria-hidden="true">
    <defs>
      <linearGradient id="bandFill" x1="0" y1="1" x2="1" y2="0">
        <stop offset="0" stop-color="#8cc63f"/>
        <stop offset="0.4" stop-color="#f0b52c"/>
        <stop offset="0.7" stop-color="#f08a2c"/>
        <stop offset="1" stop-color="#d4145a"/>
      </linearGradient>
    </defs>
    <polygon points="0,280 540,188 540,310 0,310" fill="url(#bandFill)"/>
    <line x1="0" y1="272" x2="540" y2="180" stroke="url(#bandFill)" stroke-width="3"/>
  </svg>

  <div class="wordmark"><span class="wordmark__dot"></span>Fontenot Bayou Grillhouse</div>
  <div class="divider"></div>

  <div class="owner">
    <h1 class="owner__name">DARVEL PRUITT</h1>
    <ul class="contact">
      <li class="contact__item">
        <svg class="contact__icon" viewBox="0 0 24 24"><path fill="#f0602a" d="M6.6 10.8a15 15 0 0 0 6.6 6.6l2.2-2.2c.3-.3.7-.4 1-.2 1.1.4 2.3.6 3.6.6.6 0 1 .4 1 1V20c0 .6-.4 1-1 1A17 17 0 0 1 3 4c0-.6.4-1 1-1h3.5c.6 0 1 .4 1 1 0 1.3.2 2.5.6 3.6.1.3 0 .7-.2 1z"/></svg>
        (510) 493-2615
      </li>
      <li class="contact__item">
        <svg class="contact__icon" viewBox="0 0 24 24"><rect x="2" y="5" width="20" height="14" rx="2" fill="#f0602a"/><path d="M3 6l9 7 9-7" fill="none" stroke="#050505" stroke-width="2"/></svg>
        Dpruittkr4@mailvane.example
      </li>
      <li class="contact__item">
        <svg class="contact__icon" viewBox="0 0 24 24"><path fill="#e8321e" d="M12 2a7 7 0 0 0-7 7c0 5 7 13 7 13s7-8 7-13a7 7 0 0 0-7-7zm0 9.5A2.5 2.5 0 1 1 12 6.5a2.5 2.5 0 0 1 0 5z"/></svg>
        327 Oakmere Street
      </li>
    </ul>
  </div>
</section>

</body>
</html>
```